Site Re-Design For IT/Internet Services Site

Hi, We need a redevopment of our existing website (www.talvrek.com)
Pages That need designing are:
- Content Page (existing page: http://www.talvrek.com)
- Hotspot Locations Page (existing page: Http://www.talvrek.com/hotspot-locations/hotspot-locations.asp)
- Form page layout, including textbox, checkbox, radio buttons, drop down, submit/reset buttons, "required fields error message"
- Design of our subscription "plan selection" content page (https://secure.talvrek.com/?location=1001)
- Design of the NEXT TWO pages in the above subscription form, the "email/password page, to see this select less than 3 months, 1 hour, then continue and also the credit card page, see this by filling out left hand side "new account" form and continue Specs:
- The same navigation will be retained, but should be easily modifyable via PSD file.

- NOTE THAT FOR THE DESIGN COMPETITION, ONLY the CONTENT PAGE needs to be designed

- Existing Logo to Be Maintained and COMPLETELY UNCHANGE IN ANY ASPECT
- Similar format of dual navigation required. Currently main nav is horizontal with sub nav below, and "extra" nav available on left vertical strip. Does have to stay in this format, however main nav with subnav, and "extra" nav spots must be available
- Design should be fresh and innovative
- Colors are negotiable however typical design nono's will not be accepted (black content area etc) Code Requirements:
- PSD file should contain overall design, as well as sub PSD files for navigation to be easily re-created at a later date where required.

By negotiation after sucessful design chosen, extra design aspects such as: psd cutup in html, HTML markup compatible with IE6+, Chrome, Firefox required - Seperate CSS stylesheet - Images in sub folders as appropriate may be required.

Internet

5+ pages

• black background, etc.

```html
<!DOCTYPE html>
<html lang="en">
<head>
<meta charset="utf-8">
<title>Talvrek – Wireless Solutions</title>
<link rel="stylesheet" href="https://fonts.googleapis.com/css2?family=Arimo:wght@400;700&display=swap">
<style>
:root{
  --green:#4dab12;
  --green-light:#8fd12f;
  --green-dark:#0d4d0a;
  --subnav:#2a7a0c;
  --white:#ffffff;
  --navy:#12236e;
  --link-blue:#1b2f8f;
  --orange-top:#ffbf10;
  --orange-bot:#f07800;
  --panel:#f1f1f1;
  --text:#111111;
  --icon-blue:#1f5aa8;
}
*{margin:0;padding:0;box-sizing:border-box}
html,body{width:1171px;height:1200px;overflow:hidden}
body{position:relative;background:var(--green);font-family:"Arimo",Arial,sans-serif;color:var(--text)}
.backdrop{position:absolute;left:0;top:0}
.header-photo{position:absolute;left:250px;top:0;width:921px;height:156px;
  background:linear-gradient(100deg,#ffffff 0%,#c9a98e 12%,#6b3b2a 35%,#3a1c14 60%,#8a4a22 85%,#c97a2a 100%)}
.brand{position:absolute;left:38px;top:60px;display:flex;align-items:center;gap:12px}
.brand-mark{width:34px;height:34px;background:var(--green-light)}
.brand-name{font-size:38px;font-weight:700;color:var(--icon-blue);letter-spacing:1px}
.search{position:absolute;left:408px;top:170px;font-size:14px;color:#333}
.search-row{display:flex;align-items:center;gap:8px}
.search-name{font-size:20px;font-weight:700;color:#3b6fd0}
.search-input{width:228px;height:22px;border:1px solid #8a8a8a;background:var(--white)}
.search-btn{height:22px;padding:0 10px;border:1px solid #8a8a8a;border-radius:11px;background:#eee;font-size:12px;line-height:20px}
.search-scope{display:flex;gap:14px;margin:8px 0 0 80px;font-size:12px}
.search-scope span::before{content:"";display:inline-block;width:10px;height:10px;border:1px solid #777;border-radius:50%;margin-right:5px;vertical-align:-1px}
.search-scope .on::before{background:radial-gradient(circle,#333 35%,#fff 40%)}
.quick-icons{position:absolute;left:826px;top:170px;display:flex;gap:19px}
.quick-icons svg{width:48px;height:48px}
.main-nav{position:absolute;left:40px;top:288px;display:flex;font-size:19px;color:var(--white)}
.main-nav a{color:inherit;text-decoration:none;padding:0 12px;border-right:3px dotted var(--green-light)}
.main-nav a:last-child{border-right:none}
.main-nav .current{color:var(--navy);font-weight:700;padding-left:2px}
.sub-nav{position:absolute;left:15px;top:340px;width:1142px;height:58px;background:var(--subnav);border-radius:0 0 14px 14px;display:flex;align-items:center;padding-left:22px;gap:34px;font-size:16px;color:var(--white);text-transform:uppercase}
.panel{position:absolute;top:414px;height:666px;background:var(--panel);border-radius:14px;overflow:hidden;box-shadow:0 0 4px rgba(0,0,0,.25)}
.panel-title{height:44px;background:linear-gradient(var(--orange-top),var(--orange-bot));color:var(--white);font-weight:700;font-size:19px;line-height:44px;padding-left:14px}
.jobs{left:15px;width:205px}
.jobs .panel-title{text-align:center;padding-left:0}
.jobs-body{padding:14px 8px 0 7px;font-size:12.5px;line-height:14.5px;color:var(--link-blue)}
.jobs-body p{margin-bottom:14px}
.jobs-body .plain{color:var(--text)}
.badges{position:absolute;left:12px;top:456px}
.badge-ring{width:80px;height:80px;border-radius:50%;background:#b7a8c8;margin-left:34px}
.badge-row{display:flex;gap:10px;margin-top:80px}
.badge-a{width:118px;height:62px;background:var(--white);border:2px solid #ddd}
.badge-b{width:64px;height:70px;background:linear-gradient(135deg,#2b5db8,#ffffff)}
.welcome{left:230px;width:927px}
.welcome-text{position:absolute;left:10px;top:58px;width:455px;font-size:14.6px;line-height:19px;color:var(--text)}
.welcome-text p{margin-bottom:19px}
.welcome-photo{position:absolute;left:473px;top:44px;width:454px;height:622px;background:linear-gradient(180deg,#dde8f0 0%,#b9cfe0 40%,#8aa0b4 70%,#3c4048 100%)}
.footer-text{position:absolute;left:125px;top:1163px;font-size:14.6px;color:var(--white)}
</style>
</head>
<body>
<svg class="backdrop" width="1171" height="1200" viewBox="0 0 1171 1200" aria-hidden="true">
  <rect width="1171" height="1200" fill="#4dab12"/>
  <path d="M0 0H1171V150Q900 240 500 232Q220 226 0 178Z" fill="#ffffff"/>
  <path d="M0 178Q220 226 500 232Q900 240 1171 150V175Q900 265 500 258Q220 252 0 205Z" fill="#8fd12f"/>
  <rect y="1088" width="1171" height="112" fill="#0d4d0a"/>
  <path d="M0 1150Q580 1115 1171 1150V1200H0Z" fill="#4dab12"/>
</svg>

<div class="header-photo" role="img" aria-label="Glowing fibre optic cable ends"></div>

<div class="brand"><span class="brand-mark"></span><span class="brand-name">Talvrek</span></div>

<form class="search">
  <div class="search-row"><span class="search-name">Seekly</span><span class="search-input"></span><span class="search-btn">Search</span></div>
  <div class="search-scope"><span class="on">Web</span><span>www.talvrek.com</span><span>secure.talvrek.com</span></div>
</form>

<div class="quick-icons">
  <svg viewBox="0 0 48 48"><circle cx="24" cy="24" r="23" fill="#1f5aa8"/><ellipse cx="24" cy="22" rx="12" ry="8" fill="none" stroke="#fff" stroke-width="2.5"/><path d="M18 29l-3 6 8-5" fill="#fff"/></svg>
  <svg viewBox="0 0 48 48"><circle cx="24" cy="24" r="23" fill="#1f5aa8"/><path d="M12 25L24 13 36 25M16 23V35H32V23" fill="none" stroke="#fff" stroke-width="3"/></svg>
  <svg viewBox="0 0 48 48"><circle cx="24" cy="24" r="23" fill="#1f5aa8"/><circle cx="26" cy="14" r="3" fill="#fff"/><path d="M25 20L20 36" stroke="#fff" stroke-width="4"/></svg>
  <svg viewBox="0 0 48 48"><circle cx="24" cy="24" r="23" fill="#1f5aa8"/><circle cx="16" cy="32" r="3" fill="#fff"/><path d="M14 22a12 12 0 0 1 12 12M14 14a20 20 0 0 1 20 20" fill="none" stroke="#fff" stroke-width="3"/></svg>
</div>

<nav class="main-nav">
  <a class="current">home</a><a>wireless hotspots</a><a>internet kiosks</a><a>hotspot locations</a><a>resellers</a><a>F.A.Q.</a><a>contact us</a><a>my account</a>
</nav>

<nav class="sub-nav"><span>Benefits</span><span>Demonstration</span><span>Free Site Survey</span><span>Hardware &amp; Software</span><span>&nbsp;&nbsp;How does it work?</span></nav>

<aside class="panel jobs">
  <div class="panel-title">Jobs @ Talvrek</div>
  <div class="jobs-body">
    <p>Talvrek has some exciting job offerings currently available, they are:</p>
    <p>Position: <span class="plain">Sales Manager</span><br>Location: <span class="plain">Brisbane</span><br>Description:<br><span class="plain">Talvrek is looking for a talented Sales Professional to lead the sales process. They should have exceptional customer skills and a proven background in cold calling and direct marketing.</span></p>
    <p class="plain">This position has a great base salary and exceptional commission structure which makes your earning potential unlimited!</p>
    <p class="plain">Please note that only experienced sales people need apply!</p>
  </div>
  <div class="badges">
    <div class="badge-ring"></div>
    <div class="badge-row"><div class="badge-a"></div><div class="badge-b"></div></div>
  </div>
</aside>

<main class="panel welcome">
  <div class="panel-title">Welcome to Talvrek</div>
  <div class="welcome-text">
    <p>Talvrek Wireless Solutions was founded to address the emerging and rapidly growing public demand for wireless internet access. A wireless hotspot service provision pioneer, we enable hotels, clubs, airports, motels, schools and universities, accommodation providers and cafes to offer a value added service that generates an additional revenue stream. Further information on our wireless hotspot system can be found here.</p>
    <p>Although a staggering 80% of the Australian population are now online, many are still tethered to their desks when accessing the internet. Talvrek’s vision is to create a world of ubiquitous wireless internet access, without sacrificing the rich experience you get from your office, school, or home. In today’s fast-moving world, people are used to being able to access the services they want, whenever and wherever they want them. Mobile professionals, everyday laptop-toting businessmen and students - they all need access to the internet at the push of a button, on the go.</p>
    <p>Wi-Fi is set to dramatically change the landscape of work and communication, more so than any technology since the advent of the internet. The progressive growth of Wi-Fi and its adoption across both large and small businesses, as well as through different vertical industries, means that it will soon become mainstream. All around the globe, publicly accessible wireless internet hotspots are springing up in airports, hotels, coffee shops, and restaurants. Those businesses slow on the uptake risk being left behind.</p>
  </div>
  <div class="welcome-photo" role="img" aria-label="Two colleagues working together at a laptop by a bright window"></div>
</main>

<footer class="footer-text">T: 1800 555 214 &nbsp; F: (07) 5550 1472 &nbsp; E: Contact UAll Content Copyright Talvrek Pty Ltd 2006</footer>
</body>
</html>
```